Amber Lantern Cafe Business Card

We need a business card design for a new European Cafe. Main menu will be coffee and deserts.

Requirements
Must have
• Logo - 1 of the attached versions
Address - TBA (you can use 487 Morrow Ave Unit 9 for now)
Phone - TBA (you can use 555-238-4176 for now)

```html
<!DOCTYPE html>
<html lang="en">
<head>
<meta charset="utf-8">
<title>Amber Lantern Cafe Business Card</title>
<link rel="stylesheet" href="https://fonts.googleapis.com/css2?family=Source+Sans+3:wght@400;600&display=swap">
<style>
  :root {
    --backdrop: #6d6e70;
    --card-dark: #0c0c0c;
    --card-dark-glow: #3a3a3a;
    --card-light: #ffffff;
    --ink: #1a1a1a;
    --ink-light: #ffffff;
    --swirl-front-from: #1e1e1e;
    --swirl-front-to: #8c8c8c;
    --swirl-back-from: #2a2a2a;
    --swirl-back-to: #e8e8e8;
  }
  * { margin: 0; padding: 0; box-sizing: border-box; }
  html, body {
    width: 1200px;
    height: 427px;
    overflow: hidden;
    background: var(--backdrop);
    font-family: "Source Sans 3", sans-serif;
  }
  .stage { position: relative; width: 1200px; height: 427px; }
  .card { position: absolute; overflow: hidden; }
  .card--front {
    left: 65px; top: 65px; width: 512px; height: 296px;
    background: radial-gradient(circle at 42% 38%, var(--card-dark-glow) 0%, var(--card-dark) 70%);
  }
  .card--back {
    left: 612px; top: 63px; width: 513px; height: 296px;
    background: var(--card-light);
  }
  .swirl-area { position: absolute; top: 0; height: 296px; }
  .card--front .swirl-area {
    left: 350px; width: 162px;
    background: linear-gradient(90deg, var(--swirl-front-from), var(--swirl-front-to));
  }
  .card--back .swirl-area {
    left: 0; width: 115px;
    background: linear-gradient(90deg, var(--swirl-back-from), var(--swirl-back-to));
  }
  .brand { position: absolute; display: flex; align-items: center; gap: 14px; }
  .brand__mark { display: block; border-radius: 4px; flex: none; }
  .brand__name {
    font-weight: 400; white-space: nowrap;
    display: flex; flex-direction: column; align-items: center; line-height: 1.1;
  }
  .card--front .brand { left: 35px; top: 179px; }
  .card--front .brand__mark { width: 78px; height: 84px; background: var(--ink-light); }
  .card--front .brand__name { font-size: 27px; color: var(--ink-light); }
  .card--back .brand { right: 22px; top: 25px; }
  .card--back .brand__mark { width: 66px; height: 70px; background: var(--ink); }
  .card--back .brand__name { font-size: 23px; color: var(--ink); }
  .holder {
    position: absolute; right: 15px; top: 116px;
    font-size: 16px; font-weight: 400; letter-spacing: 0.2px; color: var(--ink);
  }
  .divider {
    position: absolute; left: 166px; right: 15px; top: 147px;
    border-top: 1.5px dashed var(--ink);
  }
  .contact {
    position: absolute; right: 22px; top: 188px;
    list-style: none; text-align: right;
    font-size: 15px; line-height: 22px; color: var(--ink);
  }
  .contact__web { font-weight: 600; }
</style>
</head>
<body>
<main class="stage">
  <section class="card card--front">
    <div class="swirl-area" role="img" aria-label="Large brand swirl decoration in white on black"></div>
    <div class="brand">
      <span class="brand__mark"></span>
      <span class="brand__name"><span>Amber Lantern</span><span>Cafe</span></span>
    </div>
  </section>

  <section class="card card--back">
    <div class="swirl-area" role="img" aria-label="Large brand swirl decoration in black on white"></div>
    <div class="brand">
      <span class="brand__mark"></span>
      <span class="brand__name"><span>Amber Lantern</span><span>Cafe</span></span>
    </div>
    <p class="holder">DANIEL HARTWELL</p>
    <div class="divider"></div>
    <ul class="contact">
      <li>487 Morrow Ave Unit 9</li>
      <li>555-238-4176</li>
      <li>daniel@amberlantern.com</li>
      <li class="contact__web">www.AmberLantern.com</li>
    </ul>
  </section>
</main>
</body>
</html>
```